PowerPoint Design Project

Powerpoint design for an online marketing agency.
PP will be used as a WhitePaper to showcase our expertise.
Our USP is that we use data for marketing so the design must reflect this with charts and graphs.
A set of images is available in our pictavo account
http://www.pictavo.example/photos/qorlane/sets/48203917562084315/with/3618204957/
We already have written real content for the PP for you to work with.
Updates

1. I have added a sample of the content a 2-page extract in a word document. The full document is around 15 pages.
2. While the finished piece is to be in PowerPoint format, it will also be used as a White Paper so the design should reflect this - i.e it should be able to be read like it was a well designed Word document not just a PP
3. The design you see in the sample 2-page document is just for illustration purposes it is not intended to influence the final design at all. So for example it currently has some pull-quotes in black boxes - that is just to show what they are and I don't want the final piece to have black boxes around quotes.
4. I've been asked to make this project guaranteed: as this is the first time I've used ArtLoomly I'm going to keep it as a standard project but we are committed to the work.
5. The current deadline is for the START of design work. We need the completed design by 21 September, so there is plenty of time to schedule this in with your other work.
Many thanks
Derek 

The designs shown so far would not be suitable for turning into a WhitePaper. For example the bars across the top of the design create a break at the start of each page rather than emphasise the continuous nature of the document. 

Here is an example of some great design for a similar project - and we've uploaded another sample as a file

http://www.velmorex.example/downloads/[VELMOR]-how-teams-feel-doing-

If you asked me for some ideas on the feel of the design I would say:

1. Bold - it has to look interesting - corporate world but it doesn't need to feel dull/grey
2. Exciting 
3. Precise - easy to read , not a fussy design

Target Market(s)

Business developers, sales managers, CEOs of companies with over 5 employees but without their own marketing department

Industry/Entity Type

Marketing

Requirements
Must have
• Flawless design that says "this company is smart and means business"
Nice to have
• the powerpoint should lend itself to easy file/saveas to be delivered as a PDF and for individual slides to be extracted for presentation, or use as images in blog posts etc (so for example any page number must be easy to remove).
Should not have
• no cartoons, no line drawings, nothing to obscure easy legibility

```html
<!DOCTYPE html>
<html lang="en">
<head>
<meta charset="utf-8">
<title>How to Run a Successful Data Driven Marketing Campaign</title>
<link rel="stylesheet" href="https://fonts.googleapis.com/css2?family=Alfa+Slab+One&family=Lato:wght@300;400;700;900&family=Questrial&display=swap">
<style>
  :root {
    --bg-edge: #2f3a4c;
    --bg-mid: #6d7a8e;
    --bg-light: #b9c3d0;
    --navy: #15306e;
    --brand-blue: #1563bd;
    --accent-blue: #0b4fa6;
    --heading-blue: #1260b8;
    --band-blue: #1668c4;
    --band-dark: #0b3577;
    --body-text: #1e222a;
    --white: #ffffff;
  }
  * { margin: 0; padding: 0; box-sizing: border-box; }
  html, body { width: 1200px; height: 900px; overflow: hidden; }
  body { font-family: "Lato", Arial, sans-serif; background: var(--bg-edge); }
  .slide {
    position: relative;
    width: 1200px;
    height: 900px;
    overflow: hidden;
    background:
      linear-gradient(115deg, rgba(255,255,255,0) 25%, rgba(255,255,255,0.32) 52%, rgba(255,255,255,0) 82%),
      radial-gradient(ellipse at 55% 55%, var(--bg-light) 0%, var(--bg-mid) 55%, var(--bg-edge) 100%);
  }
  .brand {
    position: absolute;
    left: 62px;
    top: 48px;
    display: flex;
    align-items: center;
    gap: 10px;
  }
  .brand-square { width: 20px; height: 20px; background: var(--brand-blue); }
  .brand-name {
    font-weight: 900;
    font-size: 46px;
    line-height: 1;
    color: var(--brand-blue);
    letter-spacing: -1px;
  }
  .title {
    position: absolute;
    left: 294px;
    top: 38px;
    font-family: "Alfa Slab One", "Rockwell", serif;
    font-weight: 400;
    font-size: 44px;
    line-height: 44px;
    color: var(--navy);
    text-shadow: 1px 1px 0 var(--white), -1px -1px 0 rgba(255,255,255,0.6), 2px 2px 3px rgba(0,0,0,0.35);
  }
  .rule {
    position: absolute;
    left: 60px;
    top: 160px;
    width: 1095px;
    height: 2px;
    background: var(--navy);
  }
  .rule::before {
    content: "";
    position: absolute;
    left: 0;
    top: -3px;
    width: 207px;
    height: 7px;
    background: var(--navy);
  }
  .content {
    position: absolute;
    left: 72px;
    top: 226px;
    width: 672px;
    color: var(--body-text);
    font-weight: 400;
    font-size: 21px;
    line-height: 27px;
  }
  .section-heading {
    font-weight: 400;
    font-size: 27px;
    line-height: 32px;
    color: var(--heading-blue);
    margin-bottom: 26px;
  }
  .content p { margin-bottom: 18px; }
  .points { list-style: none; margin: 0 0 16px; }
  .points li {
    position: relative;
    padding-left: 30px;
    margin-bottom: 22px;
  }
  .points li::before {
    content: "";
    position: absolute;
    left: 2px;
    top: 8px;
    width: 7px;
    height: 12px;
    background: var(--navy);
    border-radius: 0 12px 12px 0;
  }
  .highlight { color: var(--accent-blue); font-weight: 700; }
  .photo-frame {
    position: absolute;
    left: 792px;
    top: 276px;
    width: 372px;
    height: 296px;
    background: var(--white);
    padding: 13px;
    transform: rotate(-1.5deg);
    box-shadow: 3px 5px 10px rgba(0,0,0,0.45);
  }
  .photo {
    width: 100%;
    height: 100%;
    background: radial-gradient(ellipse at 48% 50%, #d29a3c 0%, #8a5a1c 28%, #3a2a1e 50%, #101010 75%);
  }
  .callout {
    position: absolute;
    left: 68px;
    top: 708px;
    width: 1046px;
    height: 82px;
  }
  .callout svg { position: absolute; left: 0; top: 0; }
  .callout-text {
    position: absolute;
    left: 14px;
    top: 11px;
    width: 1000px;
    font-family: "Questrial", "Century Gothic", sans-serif;
    font-weight: 400;
    font-size: 24.5px;
    line-height: 27px;
    color: var(--white);
  }
  .page-number {
    position: absolute;
    left: 1002px;
    top: 852px;
    font-weight: 400;
    font-size: 16px;
    color: var(--body-text);
  }
  .page-bar {
    position: absolute;
    left: 1025px;
    top: 860px;
    width: 120px;
    height: 13px;
    background: repeating-linear-gradient(135deg, var(--band-blue) 0 3px, #9fc4ea 3px 5px);
  }
</style>
</head>
<body>
  <div class="slide">
    <div class="brand">
      <span class="brand-square"></span>
      <span class="brand-name">qorlane</span>
    </div>

    <h1 class="title">How to Run a Successful Data<br>Driven Marketing Campaign</h1>

    <div class="rule"></div>

    <section class="content">
      <h2 class="section-heading">Why We Need a New Science of Marketing</h2>
      <p>Traditional marketing is broken, so marketers and senior managers responsible for marketing budgets need a new game plan. Advances in technology mean our prospective clients can now:</p>
      <ul class="points">
        <li><span class="highlight">Block unwanted phone calls</span> with caller ID, and register on official do not call databases</li>
        <li><span class="highlight">Ignore sales emails</span> with sophisticated email filtering</li>
        <li><span class="highlight">Eliminate on-screen advertising</span> with pop-up blockers</li>
      </ul>
      <p>And the level of direct mail has reached such a deluge it typically ends in the recycling bin without ever having been seen: there’s a reason why marketers call it direct mail when we send it, but junk mail when we receive it.</p>
    </section>

    <figure class="photo-frame">
      <div class="photo" role="img" aria-label="Photograph of a 3D brain scan visualisation with cross-section planes on a black background"></div>
    </figure>

    <aside class="callout">
      <svg width="1046" height="82" viewBox="0 0 1046 82" aria-hidden="true">
        <polygon points="6,8 1046,8 1024,45 1046,82 6,82" fill="var(--band-dark)"/>
        <polygon points="0,2 1036,2 1012,38 1036,74 0,74" fill="var(--band-blue)"/>
        <polygon points="3,5 1030,5 1008,38 1030,71 3,71" fill="none" stroke="var(--white)" stroke-width="1.5" opacity="0.7"/>
      </svg>
      <p class="callout-text">If prospective clients can’t see or hear your current marketing and messages how can you attract leads and turn them into paying customers?</p>
    </aside>

    <span class="page-number">1</span>
    <span class="page-bar"></span>
  </div>
</body>
</html>
```